Milo's Sweet Harbor Package Design

A logo has already been made and now i need to incorporate that logo into a package design. Milo's Sweet Harbor products will be sold in retail stores and its package should appeal to both adults and children. Milo's Sweet Harbor sells candy, nuts and other snacks. Files attached will be logo files and pictures of similar package. Please refer to the files for package design. The physical package consists of a printed card (5.75 inches X 4 inches) and a plastic bag. The card is folded over the plastic bag, sealed and hole punched. The design on the card(5.75 inches X 4 inches) should consist of the logo, price(in this case it is $1.99 however it will vary for other products) and product type (in this case its apple(however it will change for other products). On the "back side"(the card is folded down the middle over the plastic and the top of the card becomes the back side, notice how in the example the top half is upside down, this is correct) should include nutrition facts, ingredients, a UPC barcode and the company information(again these vary depending on the product except for the company information that will be same for all products. Company info - "Packaged & Distributed By: Brevik Treats Supply
7142 Larchmont Ave Suite 208 Sterling Heights, Michigan 48592 586-555-0173"

TO WHOEVER WINS THE CONTEST WE WILL COMMISSION YOU TO USE THE SAME DESIGN AND ADD THE NECESSARY INFORMATION(upc, ingredients list, nutritional facts, etc) FOR THE MULTIPLE FLAVORS THAT WE WILL BE PRODUCING UNDER THE Milo's Sweet Harbor BRAND.

```html
<!DOCTYPE html>
<html lang="en">
<head>
<meta charset="utf-8">
<title>Milo's Sweet Harbor – Apple Header Card</title>
<link rel="stylesheet" href="https://fonts.googleapis.com/css2?family=Arimo:wght@400;700&family=Archivo+Black&family=Kaushan+Script&family=Pacifico&display=swap">
<style>
  :root{
    --white:#ffffff;
    --ink:#1b1414;
    --pink:#d24d77;
    --pink-light:#df6f92;
    --pink-dark:#c43f6a;
    --blue:#1273b9;
    --grey:#858381;
    --brand-blue:#1566ad;
  }
  *{margin:0;padding:0;box-sizing:border-box}
  html,body{width:1200px;height:852px;overflow:hidden;background:var(--white)}
  .card{position:relative;width:1200px;height:852px;background:var(--white);font-family:Arimo,Arial,sans-serif;color:var(--ink);border:1px solid #bbb}

  /* back panel: printed upside down so it reads correctly after folding */
  .back-panel{position:absolute;left:0;top:0;width:1200px;height:424px;transform:rotate(180deg);border-top:1px solid #666}

  .flavor-tab{position:absolute;left:536px;top:0;width:129px;height:56px;background:var(--ink);color:var(--white);
    font-family:"Archivo Black",Arial,sans-serif;font-size:24px;letter-spacing:1px;display:flex;align-items:center;justify-content:center}

  .nutrition{position:absolute;left:30px;top:37px;width:242px;height:359px;border:1px solid var(--ink);padding:3px 4px;font-size:9.5px;line-height:1.2}
  .nutrition h2{font-family:"Archivo Black",Arial,sans-serif;font-size:22px;letter-spacing:1px;line-height:1.05;font-weight:400}
  .nutrition .servings{font-size:11px;padding:1px 0}
  .nutrition .size{display:flex;justify-content:space-between;font-weight:700;font-size:12px;border-bottom:6px solid var(--ink);padding-bottom:2px}
  .nutrition .amount{font-weight:700;font-size:9px;padding-top:2px}
  .nutrition .calories{display:flex;justify-content:space-between;align-items:flex-end;font-family:"Archivo Black",Arial,sans-serif;font-size:19px;border-bottom:4px solid var(--ink);line-height:1}
  .nutrition .calories span:last-child{font-size:28px}
  .nutrition .dv{text-align:right;font-size:7px;font-weight:700;padding:2px 0;border-bottom:1px solid var(--ink)}
  .row{display:flex;justify-content:space-between;border-bottom:1px solid #777;padding:2.5px 0;font-size:10px}
  .row b{font-weight:700}
  .row.indent{padding-left:10px}
  .row.indent2{padding-left:20px}
  .row.last{border-bottom:5px solid var(--ink)}
  .nutrition .note{font-size:7px;padding-top:3px}
  .nutrition .foot{font-size:7px;padding-top:4px}

  .company{position:absolute;left:364px;top:282px;width:400px;text-align:center;font-size:20px;line-height:1.3}
  .company strong{font-family:"Archivo Black",Arial,sans-serif;font-weight:400;font-size:21px;display:block;line-height:1.3}

  .ingredients{position:absolute;left:852px;top:49px;width:300px;font-size:20px;line-height:1.38}
  .ingredients p{text-align:center}

  .barcode-space{position:absolute;left:852px;top:282px;width:300px;height:113px;background:var(--grey)}

  /* front panel */
  .front-panel{position:absolute;left:0;top:424px;width:1200px;height:428px;overflow:hidden;
    background:radial-gradient(circle at 600px 200px,var(--pink-light) 0%,var(--pink) 55%,var(--pink-dark) 100%)}
  .sunburst{position:absolute;inset:0}
  .brand{position:absolute;left:38px;top:40px;width:440px;height:340px;display:flex;align-items:center;justify-content:center;gap:14px}
  .brand-dot{width:46px;height:46px;border-radius:50%;background:var(--white);flex:none}
  .brand-name{font-family:"Archivo Black",Arial,sans-serif;font-size:40px;line-height:1.1;color:var(--white)}
  .price-burst{position:absolute;left:885px;top:20px;width:290px;height:225px}
  .price{position:absolute;left:950px;top:82px;font-family:"Archivo Black",Arial,sans-serif;font-size:50px;color:var(--white);transform:rotate(-10deg)}
  .flavor-name{position:absolute;left:948px;top:296px;font-family:"Kaushan Script",cursive;font-size:58px;color:var(--ink);transform:rotate(-5deg)}
</style>
</head>
<body>
<div class="card">

  <section class="back-panel">
    <div class="flavor-tab">APPLE</div>

    <div class="nutrition">
      <h2>Nutrition Facts</h2>
      <div class="servings">6 servings per container</div>
      <div class="size"><span>Serving size</span><span>10 pcs (10g)</span></div>
      <div class="amount">Amount Per Serving</div>
      <div class="calories"><span>Calories</span><span>110</span></div>
      <div class="dv">% Daily Value*</div>
      <div class="row"><span><b>Total Fat</b> 2.5g</span><b>3%</b></div>
      <div class="row indent"><span>Saturated Fat 1g</span><b>5%</b></div>
      <div class="row indent"><span><i>Trans</i> Fat 0g</span><span></span></div>
      <div class="row"><span><b>Sodium</b> 10mg</span><b>0%</b></div>
      <div class="row"><span><b>Total Carbohydrate</b> 22g</span><b>8%</b></div>
      <div class="row indent"><span>Dietary Fiber 0g</span><b>0%</b></div>
      <div class="row indent"><span>Total Sugars 16g</span><span></span></div>
      <div class="row indent2"><span>Includes 0g Added Sugars</span><b>0%</b></div>
      <div class="row last"><span><b>Protein</b> 0g</span><b>0%</b></div>
      <div class="note">Not a significant source of cholesterol, vitamin D, calcium, iron, and potassium</div>
      <div class="foot">* The % Daily Value (DV) tells you how much a nutrient in a serving of food contributes to a daily diet. 2,000 calories a day is used for general nutrition advice.</div>
    </div>

    <div class="company">
      <strong>Packaged &amp; Distributed</strong>
      <strong>By: Brevik Treats Supply</strong>
      7142 Larchmont Ave Suite 208 Sterling Heights,<br>Michigan 48592 586-555-0173
    </div>

    <div class="ingredients">
      <p>Ingredients:<br>Text will come here.<br>Text will come here. Text will<br>come here. Text will come<br>here. Text will come here.</p>
    </div>

    <div class="barcode-space"></div>
  </section>

  <section class="front-panel">
    <div class="sunburst" role="img" aria-label="Pink radiating sunburst background"></div>

    <div class="brand">
      <span class="brand-dot"></span>
      <span class="brand-name">Milo's<br>Sweet Harbor</span>
    </div>

    <svg class="price-burst" viewBox="0 0 290 225" aria-hidden="true">
      <polygon fill="var(--blue)" points="145,20 168,70 225,8 205,78 285,90 215,118 270,170 195,150 200,215 155,165 110,218 112,160 30,190 80,135 5,105 82,88 40,30 115,68"/>
    </svg>
    <div class="price">$1.99</div>

    <div class="flavor-name">Apple</div>
  </section>

</div>
</body>
</html>
```